We are seeking two label designs for our premium pecan snack brand, TORVELLO. TORVELLO is known for its innovative pecan snacks, specifically a healthy and exotic blend of pecans, expertly salted, and infused with unique chili flavors. Our snacks are packaged in stand-up pouch bags, and we are looking for label designs product sizes - 5 oz. ( Size: 14 x 20 cm / 5.5 x 7.8 inches / Max Capacity: 16.2 oz)

Background Information:
TORVELLO is a brand committed to offering a delightful snacking experience that combines the natural richness of pecans with the bold and exotic kick of carefully selected chilies. Our snacks cater to health-conscious consumers who appreciate the fusion of premium quality, unique flavors, and nutritional goodness.

Target Market(s)

Event Attendees (Entertainment Industry), Health-Conscious Consumers

Industry/Entity Type

Entertainment (sports events, arenas, stadiums, etc)

Font styles to use
Other font styles liked:
• Brother1816 Printed

Colors

Designer to choose colors to be used in the design.

Requirements
Must have
• Nutrition Fact (attached) , TRANSPARENT PART LIKE A WINDOW TO DISPLAY THE PRODUCT

```html
<!DOCTYPE html>
<html lang="en">
<head>
<meta charset="utf-8">
<title>TORVELLO Spicy Roasted Pecans – Pouch Label</title>
<link rel="stylesheet" href="https://fonts.googleapis.com/css2?family=Josefin+Sans:wght@300;700&family=Nunito:wght@600;800;900&display=swap">
<style>
  :root {
    --canvas: #ffffff;
    --green: #5e992c;
    --green-deep: #4c8624;
    --green-light: #c3da7c;
    --green-mid: #97bd4f;
    --ink: #1d1d1b;
    --chili: #e2572b;
    --tab: #d6d6d6;
    --tab-light: #ececec;
    --nut-dark: #6e3421;
    --nut: #9b4a2e;
    --nut-light: #c77a52;
  }
  * { box-sizing: border-box; margin: 0; padding: 0; }
  html, body { width: 1200px; height: 1200px; overflow: hidden; background: var(--canvas); }
  .canvas { position: relative; width: 1200px; height: 1200px; }

  .label {
    position: absolute; left: 260px; top: 64px;
    width: 680px; height: 1072px; overflow: hidden;
    background: linear-gradient(90deg, var(--green-deep), var(--green) 30%, var(--green) 70%, var(--green-deep));
    font-family: "Nunito", sans-serif; color: var(--ink);
  }

  .quality-tab {
    position: absolute; left: 236px; top: 0; width: 208px; height: 244px;
    background: linear-gradient(180deg, var(--tab), var(--tab-light));
    border-radius: 0 0 104px 104px;
  }
  .quality-tab__frame {
    position: absolute; left: 10px; right: 10px; top: -4px; bottom: 12px;
    border: 3px solid var(--ink); border-top: none;
    border-radius: 0 0 94px 94px;
  }
  .quality-tab__nuts {
    position: absolute; left: 28px; top: 40px; width: 152px; height: 66px;
    background: radial-gradient(ellipse at center, rgba(199,90,50,.55), rgba(199,90,50,.15) 70%, transparent);
    border-radius: 40px;
  }
  .quality-tab__text {
    position: absolute; left: 0; right: 0; top: 140px; text-align: center;
    font-weight: 900; font-size: 22px; line-height: 28px; letter-spacing: 1px;
  }
  .quality-tab__text .accent { color: var(--chili); display: block; }

  .product-line {
    position: absolute; left: 0; right: 0; top: 272px; text-align: center;
    font-family: "Josefin Sans", sans-serif; font-weight: 300; font-size: 22px; letter-spacing: 1.5px;
  }
  .brand-name {
    position: absolute; left: 0; right: 0; top: 318px; text-align: center;
    font-family: "Josefin Sans", sans-serif; font-weight: 700; font-size: 80px; line-height: 100px; letter-spacing: 2px;
  }
  .brand-maker {
    position: absolute; right: 164px; top: 428px;
    font-family: "Josefin Sans", sans-serif; font-weight: 300; font-size: 18px; letter-spacing: 1px;
  }

  .rule { position: absolute; border: 3px solid var(--ink); }
  .rule--top-box { left: 12px; top: 448px; width: 324px; height: 20px; }
  .rule--top-line { left: 12px; right: 12px; top: 456px; height: 0; border-width: 3px 0 0 0; }
  .rule--bottom-box { left: 336px; top: 982px; width: 312px; height: 20px; }
  .rule--bottom-line { left: 12px; right: 32px; top: 990px; height: 0; border-width: 3px 0 0 0; }

  .claims-band {
    position: absolute; left: 12px; right: 12px; top: 459px; height: 237px;
    background: linear-gradient(90deg, var(--green-light), #b5d06a 60%, var(--green-mid));
  }
  .pecan-illustration {
    position: absolute; left: 184px; top: 500px; width: 324px; height: 184px;
    background: radial-gradient(ellipse at 50% 50%, var(--nut-light), var(--nut) 45%, var(--nut-dark) 75%, transparent 76%);
  }
  .claim { position: absolute; text-align: center; font-size: 22px; line-height: 28px; }
  .claim .lead { display: block; color: var(--chili); font-weight: 600; letter-spacing: .5px; }
  .claim .main { display: block; font-weight: 800; }
  .claim--salted { left: 52px; top: 486px; width: 110px; }
  .claim--chili { left: 470px; top: 478px; width: 110px; }
  .claim--snack { left: 512px; top: 564px; width: 150px; }
  .claim--exotic { left: 22px; top: 612px; width: 150px; }
  .claim-arrows { position: absolute; left: 0; top: 0; width: 680px; height: 1072px; pointer-events: none; }

  .product-window {
    position: absolute; left: 20px; top: 696px; width: 640px; height: 200px;
    background:
      radial-gradient(ellipse at 30% 40%, rgba(255,255,255,.35), transparent 45%),
      linear-gradient(110deg, #8a5a3c, #a86f49 35%, #6f4127 60%, #9b6340 85%, #7a4a2e);
  }
  .lower-band {
    position: absolute; left: 32px; right: 32px; top: 896px; height: 94px;
    background: linear-gradient(90deg, var(--green-mid), var(--green-light) 30%, var(--green-mid));
  }

  .net-weight {
    position: absolute; left: 56px; top: 940px; width: 104px; height: 104px;
    border-radius: 50%; background: #ffffff; border: 4px solid #d8d8d8;
    text-align: center;
  }
  .net-weight__ring {
    position: absolute; inset: 6px; border: 2px solid var(--ink); border-radius: 50%;
  }
  .net-weight__label { position: absolute; left: 0; top: 0; width: 104px; height: 104px; }
  .net-weight__value {
    position: absolute; left: 0; right: 0; top: 44px;
    color: var(--chili); font-weight: 900; font-size: 22px; line-height: 22px;
  }
  .net-weight__metric {
    position: absolute; left: 0; right: 0; top: 68px;
    font-weight: 600; font-size: 13px;
  }
</style>
</head>
<body>
<div class="canvas">
  <section class="label">
    <div class="quality-tab">
      <div class="quality-tab__frame"></div>
      <div class="quality-tab__nuts" role="img" aria-label="Hand-drawn pecan sketch in chili orange"></div>
      <p class="quality-tab__text"><span class="accent">PREMIUM</span>QUALITY</p>
    </div>

    <p class="product-line">SPICY ROASTED PECANS</p>
    <h1 class="brand-name">TORVELLO</h1>
    <p class="brand-maker">BY HALDEN</p>

    <div class="claims-band"></div>
    <div class="rule rule--top-line"></div>
    <div class="rule rule--top-box"></div>

    <div class="pecan-illustration" role="img" aria-label="Illustration of a pile of roasted pecan halves"></div>

    <p class="claim claim--salted"><span class="lead">expertly</span><span class="main">salted</span></p>
    <p class="claim claim--chili"><span class="lead">chili</span><span class="main">flavors</span></p>
    <p class="claim claim--snack"><span class="lead">innovative</span><span class="main">snack</span></p>
    <p class="claim claim--exotic"><span class="lead">healthy</span><span class="main">and exotic</span></p>

    <svg class="claim-arrows" viewBox="0 0 680 1072" fill="none" stroke="#1d1d1b" stroke-width="2.5" stroke-linecap="round" stroke-linejoin="round" aria-hidden="true">
      <path d="M168 598 C150 606 132 600 134 588 C136 576 154 578 150 590 C144 604 120 600 112 572"/>
      <path d="M104 582 L112 570 L120 582"/>
      <path d="M424 548 C420 530 430 520 442 522 C454 526 450 540 440 538 C428 534 440 508 468 508"/>
      <path d="M458 500 L470 508 L460 516"/>
      <path d="M196 620 C196 650 172 660 152 640"/>
      <path d="M150 630 L150 642 L162 642"/>
      <path d="M498 636 C510 670 560 682 580 644"/>
      <path d="M572 650 L580 640 L586 652"/>
    </svg>

    <div class="product-window" role="img" aria-label="Clear window showing the roasted pecans inside the pouch"></div>
    <div class="lower-band"></div>
    <div class="rule rule--bottom-line"></div>
    <div class="rule rule--bottom-box"></div>

    <div class="net-weight">
      <div class="net-weight__ring"></div>
      <svg class="net-weight__label" viewBox="0 0 104 104" aria-hidden="true">
        <defs><path id="weight-arc" d="M22 52 A30 30 0 0 1 82 52"/></defs>
        <text font-family="Nunito, sans-serif" font-weight="800" font-size="12" fill="#1d1d1b">
          <textPath href="#weight-arc" startOffset="50%" text-anchor="middle">Net Weight</textPath>
        </text>
      </svg>
      <p class="net-weight__value">5 oz.</p>
      <p class="net-weight__metric">(142 gr.)</p>
    </div>
  </section>
</div>
</body>
</html>
```